Harbor Yield Group brochure

I need a standard 8 1/2 x 11 brochure and it must have a place for addresses and a stamp to mail located on the back (meet US postal requirements). I have logo and copy but will need a few unique images/icons to make it look great. I am a start up business development company that specializes in lead generation, blogging, social media, etc. Brochure must stand out in the mail and have that wow factor but must be clean as well. I would also like the topics provided to not stay within the lines of the folds on the brochure. Would like it to be free flowing without boundaries.

Please do no include the wine logo

Industry/Entity Type

Group

```html
<!DOCTYPE html>
<html lang="en">
<head>
<meta charset="utf-8">
<title>Harbor Yield Group – Brochure Inside Spread</title>
<link rel="stylesheet" href="https://fonts.googleapis.com/css2?family=Cabin:ital,wght@0,400;0,500;0,600;1,400&family=Cabin+Condensed:wght@500;600&display=swap">
<style>
  :root {
    --teal-dark: #0e5a5b;
    --teal: #00a6b6;
    --teal-light: #48c3c6;
    --red: #d8302a;
    --ink: #3a3a3a;
    --muted: #6a6a6a;
    --paper: #ffffff;
    --backdrop: #eeeeee;
  }
  * { box-sizing: border-box; margin: 0; padding: 0; }
  html, body { width: 1200px; height: 1000px; overflow: hidden; background: var(--backdrop); }
  body { font-family: "Cabin", sans-serif; color: var(--ink); }

  .spread {
    position: absolute; left: 0; top: 34px;
    width: 870px; height: 675px;
    background: var(--paper);
    transform: scale(1.3793); transform-origin: 0 0;
  }
  .abs { position: absolute; }

  .section-arc { position: absolute; }
  .section-title { position: absolute; color: var(--teal-dark); line-height: 1.2; }
  .section-title strong { font-weight: 500; font-size: 14px; display: block; }
  .section-title span { font-size: 12.5px; display: block; }
  .title-blue strong { color: var(--teal); }

  .tagline { position: absolute; font-style: italic; font-size: 9.5px; line-height: 1.35; color: var(--teal-dark); }
  .copy { position: absolute; font-size: 9.6px; line-height: 13.2px; color: var(--ink); }
  .small-copy { position: absolute; font-size: 8.6px; line-height: 13.2px; color: var(--muted); }
  .caption { position: absolute; font-size: 6.4px; line-height: 1.4; color: var(--muted); text-align: center; }
  .note { position: absolute; font-size: 7.4px; line-height: 1.55; color: var(--muted); }
  .note b { color: var(--ink); font-weight: 500; }

  .pie { position: absolute; width: 48px; height: 48px; }

  .chart-axis { position: absolute; background: #b9c7cc; }
  .bar {
    position: absolute; bottom: 203px;
    font-family: "Cabin Condensed", sans-serif; font-weight: 600;
    color: #fff; text-transform: uppercase; text-align: center;
    line-height: 0.95; padding-top: 14px;
  }
  .bar .big { font-size: 17px; display: block; }
  .bar .mid { font-size: 12px; display: block; }
  .bar .sm { font-size: 7.2px; display: block; line-height: 1.05; }
  .bar-dark { background: var(--teal-dark); }
  .bar-teal { background: var(--teal); }
  .bar-light { background: var(--teal-light); }
  .bar .rule { display: block; height: 1px; background: rgba(255,255,255,.6); margin: 3px 4px; }
  .bar .accent { color: var(--red); }
  .bar-kicker { position: absolute; font-family: "Cabin Condensed", sans-serif; font-weight: 600; font-size: 7.5px; color: var(--red); line-height: 1; text-align: center; }

  .specialties {
    position: absolute; left: 737px; top: 3px; width: 122px; height: 146px;
    background: var(--teal); color: #fff; padding: 26px 8px 0;
    font-size: 6.4px; line-height: 13px;
  }
  .specialties em { display: block; font-style: italic; }
  .specialties ul { list-style: none; }

  .art { position: absolute; }
  .www { position: absolute; font-size: 21px; font-weight: 600; letter-spacing: 1px; color: var(--teal-dark); }
</style>
</head>
<body>
<main class="spread">

  <!-- Strategic Brand Positioning -->
  <svg class="section-arc" style="left:22px;top:34px" width="50" height="64" viewBox="0 0 50 64">
    <path d="M48 6 A28 28 0 0 0 16 58" fill="none" stroke="var(--teal-dark)" stroke-width="10"/>
  </svg>
  <h2 class="section-title" style="left:50px;top:56px"><strong>Strategic</strong><span>Brand Positioning</span></h2>
  <p class="tagline" style="left:22px;top:122px">It's all about the Experience!</p>
  <p class="copy" style="left:22px;top:160px;width:232px">Great brands always start with a plan and nothing matters more to your business than your perceived value to potential customers. As you know, there are many other competitors in your niche. The process of becoming #1 can be extremely complicated because quite frankly every business niche is unique. Harbor Yield Group will position your business as the most recognized brand in your niche and THE ONLY LOGICAL CHOICE!</p>

  <svg class="pie" style="left:35px;top:292px" viewBox="0 0 48 48">
    <circle cx="24" cy="24" r="24" fill="var(--teal-dark)"/>
    <path d="M24 24 L8 36 A20 20 0 0 0 40 36 Z" fill="var(--teal)"/>
    <circle cx="24" cy="24" r="11" fill="#fff"/>
    <path d="M24 24 L12 33 L24 27 L36 33 Z" fill="var(--teal-dark)"/>
  </svg>
  <svg class="pie" style="left:121px;top:292px" viewBox="0 0 48 48">
    <circle cx="24" cy="24" r="24" fill="var(--teal-dark)"/>
    <path d="M24 24 L24 8 A16 16 0 0 1 38 32 Z" fill="var(--teal)"/>
  </svg>
  <svg class="pie" style="left:207px;top:292px" viewBox="0 0 48 48">
    <circle cx="24" cy="24" r="24" fill="var(--teal)"/>
    <path d="M24 24 L24 8 A16 16 0 0 1 38 32 Z" fill="var(--teal-dark)"/>
  </svg>

  <p class="small-copy" style="left:22px;top:374px;width:78px">Logos, color schemes and fonts play an important role in brand position but the most important piece in separating your brand from the rest is the experience potential customers associate your company with. This is the hardest part when creating a unique and recognizable brand.</p>
  <p class="small-copy" style="left:108px;top:374px;width:78px">Create a unique action plan that includes marketing, community involvement, increased website traffic, press releases and modifying your current public relations plan.</p>
  <p class="small-copy" style="left:194px;top:374px;width:78px">After you become the only logical choice in your niche, the last step is keeping your business #1. The creation of a master strategic plan will allow you to keep top of mind awareness for years to come.</p>

  <!-- Blogging -->
  <h2 class="section-title title-blue" style="left:300px;top:56px;width:126px;text-align:right"><strong>Blogging</strong><span style="color:var(--teal-dark)">to Generate Revenue</span></h2>
  <svg class="section-arc" style="left:410px;top:34px" width="50" height="64" viewBox="0 0 50 64">
    <path d="M2 6 A28 28 0 0 1 34 58" fill="none" stroke="var(--teal)" stroke-width="10"/>
  </svg>
  <p class="tagline" style="left:313px;top:120px;width:120px">Not just for Nerds, Hipsters and Techies!</p>
  <p class="copy" style="left:313px;top:160px;width:152px">Blogging has become so powerful if you are not blogging your company is falling in Seekwell Search rankings (SEO). A recent study suggests businesses in the top 3 Seekwell rankings generate 61.5% of the traffic. More website traffic paired with compelling online marketing content leads to more sales.</p>

  <div class="chart-axis" style="left:305px;top:295px;width:1px;height:180px"></div>
  <div class="chart-axis" style="left:305px;top:474px;width:265px;height:1px"></div>

  <div class="bar bar-dark" style="left:325px;width:38px;height:160px">
    <span class="big">77%</span><span class="big">OF</span><span class="sm">Internet</span><span class="mid">Users</span><span class="mid">Read</span><span class="mid">Blogs</span>
  </div>
  <div class="bar bar-dark" style="left:372px;width:38px;height:137px">
    <span class="big">57%</span><span class="big">OF</span><span class="sm">Companies</span><span class="mid">With</span><span class="mid">A</span><span class="sm">Blog have acquired a customer</span><span class="mid">From</span><span class="mid">Their</span><span class="sm">Blog</span>
  </div>
  <div class="bar bar-dark" style="left:419px;width:38px;height:140px">
    <span class="big">61%</span><span class="big">OF</span><span class="sm">Consumers</span><span class="mid">Have</span><span class="sm">Made purchase</span><span class="mid">Based</span><span class="mid">On</span><span class="mid">Blog</span>
  </div>
  <div class="bar bar-teal" style="left:465px;width:43px;height:472px;padding-top:30px">
    <span class="rule"></span><span class="sm">Websites</span><span class="mid">With</span><span class="mid">Blogs</span><span class="mid">Have</span><span class="mid">434%</span><span class="sm">More<br>Indexed<br>Pages</span><span class="rule"></span>
  </div>
  <p class="bar-kicker" style="left:508px;top:266px;width:44px">MOST<br><span style="font-size:5px">IMPORTANTLY!</span></p>
  <div class="bar bar-light" style="left:512px;width:36px;height:188px;padding-top:12px">
    <span class="rule"></span><span class="sm">Small<br>Businesses</span><span class="mid">With</span><span class="mid">Blogs</span><span class="sm">Generate</span><span class="mid accent">126%</span><span class="mid">More</span><span class="mid">Leads</span>
  </div>

  <p class="small-copy" style="left:313px;top:498px;width:82px">We help you turn a blog into a MONEY making machine for your business:</p>
  <p class="small-copy" style="left:313px;top:564px;width:82px">We will teach you the correct way to blog and how to avoid some of the blogging blunders.</p>

  <svg class="abs" style="left:423px;top:500px" width="34" height="34" viewBox="0 0 34 34">
    <path d="M17 3 A14 14 0 1 1 4 12" fill="none" stroke="var(--red)" stroke-width="1.6"/>
    <path d="M1 9 L4 13 L8 10" fill="none" stroke="var(--red)" stroke-width="1.6"/>
    <path d="M17 10 V18 H23" fill="none" stroke="var(--red)" stroke-width="1.6"/>
  </svg>
  <p class="caption" style="left:405px;top:540px;width:70px">Spending too much time setting up a blog</p>
  <div class="art" role="img" aria-label="Audience icon" style="left:505px;top:500px;width:36px;height:30px;background:var(--red);border-radius:6px 6px 2px 2px"></div>
  <p class="caption" style="left:480px;top:540px;width:86px">Not knowing your audience</p>
  <svg class="abs" style="left:423px;top:573px" width="34" height="34" viewBox="0 0 34 34">
    <circle cx="17" cy="17" r="16" fill="var(--red)"/>
    <circle cx="17" cy="17" r="11" fill="none" stroke="#fff" stroke-width="1.2"/>
  </svg>
  <p class="caption" style="left:405px;top:613px;width:70px">No 'call of action'</p>
  <svg class="abs" style="left:507px;top:573px" width="34" height="34" viewBox="0 0 34 34">
    <rect width="34" height="34" fill="var(--red)"/>
    <rect x="6" y="6" width="22" height="22" fill="none" stroke="#fff" stroke-width="1"/>
  </svg>
  <p class="caption" style="left:478px;top:613px;width:92px">Lack of compelling engaging content</p>

  <!-- Lead Generation -->
  <h2 class="section-title title-blue" style="left:597px;top:40px;width:120px;text-align:center"><strong>Lead Generation</strong><span>and conversion</span></h2>
  <svg class="section-arc" style="left:626px;top:72px" width="64" height="30" viewBox="0 0 64 30">
    <path d="M5 2 A27 24 0 0 0 59 2" fill="none" stroke="var(--teal)" stroke-width="9"/>
  </svg>
  <p class="tagline" style="left:600px;top:120px;width:120px">Just like speed dating… Well maybe not!</p>
  <p class="copy" style="left:600px;top:160px;width:132px">Ever wondered why a few businesses seem like they have so many leads they have to turn business away? It's simple, they generate a massive amount of leads. Consumers don't buy from every business they come into contact with so having tons of leads in your pipeline will make your business very profitable. You're not a rocket scientist and neither are we, but we both know more leads translate into more sales!</p>

  <aside class="specialties">
    <em>Our other specialties:</em>
    <ul>
      <li>Website Design &amp; Creation</li>
      <li>Traditional Marketing Methods</li>
      <li>Public Relations</li>
      <li>SEO (Search Engine Optimization)</li>
      <li>Event Management</li>
      <li>Database/Email marketing</li>
      <li>Social Media Management</li>
    </ul>
  </aside>

  <div class="art" role="img" aria-label="Illustration of a box with social media icons" style="left:752px;top:172px;width:58px;height:76px;background:linear-gradient(160deg,var(--teal-light),var(--teal-dark))"></div>
  <p class="caption" style="left:735px;top:262px;width:92px">Using social media sites</p>

  <p class="www" style="left:618px;top:362px">WWW</p>
  <p class="caption" style="left:598px;top:418px;width:104px">Using your website and blog</p>

  <div class="art" role="img" aria-label="Illustration of an open envelope with dollar sign and wow burst" style="left:752px;top:325px;width:60px;height:70px;background:linear-gradient(160deg,var(--teal),var(--teal-dark))"></div>
  <p class="note" style="left:737px;top:417px;width:110px;text-align:left">Capturing more emails and creating special offers for potential customers</p>

  <div class="art" role="img" aria-label="Illustration of an envelope with rising bar chart" style="left:626px;top:490px;width:56px;height:62px;background:linear-gradient(160deg,var(--teal-light),var(--teal-dark))"></div>
  <p class="note" style="left:600px;top:575px;width:120px">Using direct mail and other traditional marketing efforts which you are easily able to track results and see the impact of motivating offers.</p>

  <div class="art" role="img" aria-label="Illustration of an envelope with wow offers lettering" style="left:740px;top:490px;width:84px;height:56px;background:linear-gradient(160deg,var(--teal-light),var(--teal-dark))"></div>
  <p class="note" style="left:728px;top:575px;width:118px">Creating compelling email offers to your current database *<b>businesses typically don't understand how to make money from their current customers.</b></p>

</main>
</body>
</html>
```